Etiketten-Design für Qualitäts- und Prädikatswein
Zielgruppe
Qualitäts- und Prädikatsweine
Aufgabenstellung
Das Etikett muss auf der Weinflasche zweigeteilt sein.
Etikett vorne: Höhe 14,5 cm x Breite 6 cm:
Auf der Vorderseite sollen folgende Daten mit enthalten sein (Reihenfolge ist frei wählbar):
- Unser Logo (Datei: Logo)
- Name des Weins z.B. Velora
- Kategorie z.B. Beerenauslese
- Geschmackskategorie z.B. süß
- Jahrgang z.B. 2023
- Austria
Rückenetikett (Beispiel: Datei Rückenetikett): Höhe 11 cm x Breite 6 cm
Auf der Rückseite müssen folgende Daten vorhanden sein (Reihenfolge ist frei wählbar):
- Logo ganz oben
- Verkehrsbezeichnungen (Schriftgröße mind. 1,2 mm): Prädikatswein LN 4827163
- Herkunft (Schriftgröße mind. 1,2 mm): Wein aus Österreich Burgenland
- Nennvolumen (Schriftgröße mind. 6 mm): e 0,5 L
- Alkoholgehalt (Schriftgröße mind. 1,2 mm): Alc. 8,5 % Vol.
- Restzuckergehalt (Schriftgröße mind. 1,2 mm): süß
- Zutaten (Schriftgröße mind. 1,2 mm): Zutaten und ein QR-Code
- Platz für ein Zertifizierungslogo
- Allergenkennzeichnung (Schriftgröße mind. und max. 1,2 mm): Enthält Sulfite
- Abfüller (Schriftgröße mind. 1,2 mm):
Vertrieb:
Kalmor Nerisa GmbH
A-4638 Gols
www.kalmor-nerisa.com
Abfüller 5361842 A-4638 <---- (Schriftgröße mind. und max. 1,2 mm)
Kalmor Solenn ArtikelNr.: 3815/46
Da wir vor allem Prädikatsweine mit höchster Qualität herstellen, soll das Etikett dies auch wiederspiegeln. Den Hintergrund stellen wir uns schwarz vor. Der Hintergrund darf auch gerne eine grafische Musterrung beinhalten.
Alle Angaben müssen sich in den Dateien bearbeitbar sein, da sich diese Daten zum teil noch ändern werden. Die Dateien müssen wir Druckereien geeignet sein.
Update: Das Flaschenmaß ist Höhe 30 cm, Durchmesser unten 6 cm. Es handelt sich also um eine schlanke Flasche. Siehe Datei: Flasche

```html
<!DOCTYPE html>
<html lang="de">
<head>
<meta charset="utf-8">
<title>Velora – Frontetikett</title>
<link rel="stylesheet" href="https://fonts.googleapis.com/css2?family=Cinzel:wght@500&family=Playfair+Display:ital,wght@0,400;1,400&family=Montserrat:wght@400&display=swap">
<style>
  :root {
    --page: #ffffff;
    --label-black: #050505;
    --wine-red: #b8081f;
    --gold: #c9982c;
    --white: #f4f4f4;
    --rule: #bdbdbd;
    --vintage-red: #a3162a;
    --origin-grey: #8a8a8a;
  }
  html, body {
    margin: 0;
    width: 1200px;
    height: 1125px;
    overflow: hidden;
    background: var(--page);
  }
  .front-label {
    position: absolute;
    left: 400px;
    top: 80px;
    width: 400px;
    height: 966px;
    background: var(--label-black);
    overflow: hidden;
  }
  .label-crest {
    position: absolute;
    left: 0;
    top: 0;
    width: 400px;
    height: 220px;
  }
  .brand-name {
    position: absolute;
    left: 0;
    width: 400px;
    top: 218px;
    margin: 0;
    text-align: center;
    font-family: "Cinzel", serif;
    font-weight: 500;
    font-size: 31px;
    letter-spacing: 1px;
    color: var(--gold);
  }
  .title-rule {
    position: absolute;
    left: 45px;
    width: 310px;
    height: 1px;
    background: var(--rule);
  }
  .title-rule--top { top: 311px; }
  .title-rule--bottom { top: 391px; }
  .wine-name {
    position: absolute;
    left: 0;
    width: 400px;
    top: 312px;
    margin: 0;
    text-align: center;
    font-family: "Playfair Display", serif;
    font-weight: 400;
    font-size: 64px;
    line-height: 78px;
    letter-spacing: 4px;
    color: var(--white);
  }
  .wine-category {
    position: absolute;
    left: 0;
    width: 400px;
    top: 414px;
    margin: 0;
    text-align: center;
    font-family: "Montserrat", sans-serif;
    font-size: 21px;
    letter-spacing: 4px;
    color: var(--white);
  }
  .vine-leaves {
    position: absolute;
    left: 285px;
    top: 470px;
    width: 115px;
    height: 400px;
    background: radial-gradient(ellipse at 70% 45%, #4a4a4a 0%, #363636 50%, rgba(5,5,5,0) 80%);
  }
  .vintage, .taste {
    position: absolute;
    left: 78px;
    width: 240px;
    margin: 0;
    text-align: center;
    font-family: "Playfair Display", serif;
    font-style: italic;
    color: var(--vintage-red);
  }
  .vintage {
    top: 572px;
    font-size: 18px;
    letter-spacing: 12px;
  }
  .taste {
    top: 622px;
    font-size: 17px;
    letter-spacing: 6px;
  }
  .vine-tree {
    position: absolute;
    left: 118px;
    top: 773px;
    width: 165px;
    height: 75px;
    background: radial-gradient(ellipse at 50% 45%, #bcbcbc 0%, #7d7d7d 45%, rgba(5,5,5,0) 72%);
  }
  .origin {
    position: absolute;
    left: 0;
    width: 400px;
    top: 872px;
    margin: 0;
    text-align: center;
    font-family: "Montserrat", sans-serif;
    font-size: 13px;
    letter-spacing: 9px;
    color: var(--origin-grey);
  }
</style>
</head>
<body>
  <main class="front-label">
    <svg class="label-crest" viewBox="0 0 400 220" aria-hidden="true">
      <rect x="0" y="0" width="400" height="76" fill="var(--wine-red)"/>
      <polygon points="67,75 333,75 200,212" fill="var(--wine-red)"/>
      <circle class="brand-mark" cx="200" cy="128" r="44" fill="none" stroke="var(--gold)" stroke-width="3"/>
    </svg>
    <p class="brand-name">Kalmor Solenn</p>

    <span class="title-rule title-rule--top"></span>
    <h1 class="wine-name">VELORA</h1>
    <span class="title-rule title-rule--bottom"></span>
    <p class="wine-category">BEERENAUSLESE</p>

    <div class="vine-leaves" role="img" aria-label="Weinblätter und Traube als dunkelgraue Illustration"></div>

    <p class="vintage">2023</p>
    <p class="taste">süß</p>

    <div class="vine-tree" role="img" aria-label="Gezeichneter Rebstock in Silbergrau"></div>

    <p class="origin">AUSTRIA</p>
  </main>
</body>
</html>
```